Visitenkarte und Briefpapier für Rechtsanwaltskanzlei
Zielgruppe
Neugründung einer Rechtsanwaltskanzlei für Strafrecht mit einem Anwalt
Aufgabenstellung
Ich möchte gerne Briefpapier und Visitenkarten mit einem schlichten aber professionellen Charakter für meine neue Rechtsanwaltskanzlei erstellen lassen. Die Erscheinung soll modern, sachlich und klar sein. Es soll kein Logo verwendet werden, sondern nur der Namensschriftzug "Dr. Anselm Wiegand", gerne in Großbuchstaben. Siehe dazu beispielhaft die Design-Charakter der angegeben Links.
Die Visitenkarte sollen als druckfähiges PDF und das Briefpapier zusätzlich als Word-Dokument geliefert werden.

```html
<!DOCTYPE html>
<html lang="de">
<head>
<meta charset="utf-8">
<title>Visitenkarte – Dr. Anselm Wiegand</title>
<link href="https://fonts.googleapis.com/css2?family=Cinzel:wght@400&family=Courier+Prime:wght@400;700&family=Tinos:wght@700&display=swap" rel="stylesheet">
<style>
  :root {
    --backdrop: #ececec;
    --navy: #121c4c;
    --paper: #fbfbfb;
    --silver: #c9cbd3;
    --name-grey: #8d8f94;
    --rule-grey: #b9babd;
    --contact-white: #f1f2f6;
  }
  * { margin: 0; padding: 0; box-sizing: border-box; }
  html, body {
    width: 1200px;
    height: 800px;
    overflow: hidden;
    background: var(--backdrop);
  }
  .canvas {
    position: relative;
    width: 1200px;
    height: 800px;
    display: flex;
    align-items: center;
    justify-content: center;
    gap: 44px;
  }
  .card {
    position: relative;
    width: 530px;
    height: 322px;
    box-shadow: 0 2px 6px rgba(0,0,0,0.12);
  }
  /* Rückseite */
  .card--back {
    background: var(--navy);
  }
  .back__firm {
    position: absolute;
    left: 44px;
    top: 112px;
    font-family: "Cinzel", serif;
    font-size: 17px;
    letter-spacing: 0.04em;
    color: var(--silver);
  }
  .back__contact {
    position: absolute;
    right: 28px;
    bottom: 30px;
    text-align: center;
    font-family: "Courier Prime", monospace;
    font-weight: 700;
    font-size: 11.5px;
    line-height: 1.75;
    color: var(--contact-white);
  }
  /* Vorderseite */
  .card--front {
    background: var(--paper);
  }
  .front__block {
    position: absolute;
    left: 120px;
    top: 104px;
    width: 300px;
    text-align: right;
  }
  .front__name {
    font-family: "Cinzel", serif;
    font-size: 27px;
    letter-spacing: 0.03em;
    color: var(--name-grey);
    white-space: nowrap;
  }
  .front__rule {
    height: 4px;
    background: var(--rule-grey);
    margin: 6px 0 8px;
  }
  .front__firm {
    font-family: "Tinos", serif;
    font-weight: 700;
    font-size: 14px;
    color: var(--navy);
  }
</style>
</head>
<body>
  <main class="canvas">
    <section class="card card--back" aria-label="Rückseite der Visitenkarte">
      <p class="back__firm">Rechtsanwaltskanzlei für Strafrecht</p>
      <address class="back__contact" style="font-style:normal">
        Lindenallee 8 28195 Falkenau<br>
        Tel.: +49 (0)421 3860512 Fax: +49 (0)421 3860519<br>
        mail: info@anselm-wiegand.de web: www.anselm-wiegand.de
      </address>
    </section>

    <section class="card card--front" aria-label="Vorderseite der Visitenkarte">
      <div class="front__block">
        <h1 class="front__name">Dr. Anselm Wiegand</h1>
        <div class="front__rule"></div>
        <p class="front__firm">Rechtsanwaltskanzlei für Strafrecht</p>
      </div>
    </section>
  </main>
</body>
</html>
```